Bref créative
Modern Business Name Card for IT Company
qLumio Sdn Bhd
Simple
Marissa Tanaka
Senior Manager
Lot C-17, 5B Floor,
8 Kilner Plaza,
No. 7, Jalan 24/6
47810 Petaling Jaya
Selangor, Malaysia
marissa@qlumiomarketing.example
www.qlumiomarketing.example
2187605-K
Kindly change the tagline of the website to a different font Segoe UI Semibold since the current font seem to rough and thick. Thanks.

```html
<!DOCTYPE html>
<html lang="en">
<head>
<meta charset="utf-8">
<title>qLumio Sdn Bhd – Business Card</title>
<link rel="stylesheet" href="https://fonts.googleapis.com/css2?family=Open+Sans:wght@400;600;700&display=swap">
<style>
  :root {
    --page-bg: #e4e5e7;
    --card-white: #ffffff;
    --brand-blue: #1a5fc4;
    --brand-blue-deep: #0b3c93;
    --brand-blue-light: #3c8ae6;
    --olive: #8a9a2e;
    --text-blue: #1d4f9e;
    --text-white: #ffffff;
    --logo-blue: #1a56b8;
  }
  * { box-sizing: border-box; margin: 0; padding: 0; }
  html, body {
    width: 1200px; height: 842px; overflow: hidden;
    background: var(--page-bg);
    font-family: "Open Sans", Arial, sans-serif;
  }
  .canvas {
    position: relative; width: 1200px; height: 842px;
    display: flex; align-items: center; justify-content: center; gap: 40px;
  }
  .card {
    position: relative; width: 540px; height: 309px; overflow: hidden;
    box-shadow: 0 6px 18px rgba(0,0,0,0.18);
  }

  /* Front */
  .card-front { background: var(--card-white); }
  .brand {
    position: absolute; left: 34px; top: 44px;
    display: flex; align-items: center; gap: 12px;
  }
  .brand-dot {
    width: 40px; height: 40px; border-radius: 50%;
    background: var(--brand-blue);
  }
  .brand-name {
    font-size: 46px; font-weight: 700; color: var(--logo-blue);
    letter-spacing: 1px; line-height: 1;
  }
  .contact-panel {
    position: absolute; left: 208px; top: 140px; right: 0; bottom: 0;
    background: linear-gradient(160deg, var(--brand-blue-light) 0%, var(--brand-blue) 45%, var(--brand-blue-deep) 100%);
  }
  .name-band {
    position: absolute; left: 0; top: 140px; width: 208px; height: 56px;
    background: var(--olive); padding: 11px 0 0 22px; color: var(--text-white);
  }
  .person-name { font-size: 12px; font-weight: 700; letter-spacing: 1.5px; text-transform: uppercase; }
  .person-title { font-size: 10px; letter-spacing: 1.2px; text-transform: uppercase; margin-top: 3px; }
  .address {
    position: absolute; left: 22px; top: 210px;
    font-size: 9.5px; line-height: 15px; color: var(--text-blue);
    text-transform: uppercase; letter-spacing: 0.6px;
  }
  .contact-list {
    position: absolute; left: 238px; top: 214px; list-style: none;
    color: var(--text-white); font-size: 9.5px; line-height: 15px; letter-spacing: 0.5px;
  }
  .contact-list li { display: flex; align-items: center; gap: 6px; }
  .contact-list svg { width: 9px; height: 9px; flex: none; }

  /* Back */
  .card-back {
    background: radial-gradient(circle at 78% 62%, var(--brand-blue-light) 0%, var(--brand-blue) 40%, var(--brand-blue-deep) 100%);
  }
  .website-tagline {
    position: absolute; left: 34px; top: 108px;
    font-family: "Open Sans", "Segoe UI", sans-serif; font-weight: 600;
    font-size: 19px; letter-spacing: 3px; color: var(--text-white);
    text-transform: uppercase;
  }
</style>
</head>
<body>
<main class="canvas">
  <section class="card card-front" aria-label="Business card front">
    <div class="brand">
      <span class="brand-dot"></span>
      <span class="brand-name">qLumio</span>
    </div>
    <div class="contact-panel"></div>
    <div class="name-band">
      <p class="person-name">Marissa Tanaka</p>
      <p class="person-title">Senior Manager</p>
    </div>
    <address class="address" style="font-style:normal">
      Lot C-17, 5B Floor,<br>
      8 Kilner Plaza,<br>
      No. 7, Jalan 24/6<br>
      47810 Petaling Jaya<br>
      Selangor, Malaysia
    </address>
    <ul class="contact-list">
      <li><svg viewBox="0 0 10 10"><circle cx="5" cy="5" r="5" fill="#fff"/><path d="M3 2.5h1.2l.5 1.5-.7.6a4 4 0 0 0 1.4 1.4l.6-.7 1.5.5V7A.8.8 0 0 1 6.7 7.8 4.8 4.8 0 0 1 2.2 3.3.8.8 0 0 1 3 2.5z" fill="#1a5fc4"/></svg>603-5521 0486</li>
      <li><svg viewBox="0 0 10 10"><circle cx="5" cy="5" r="5" fill="#fff"/><rect x="2.4" y="3.2" width="5.2" height="3.6" fill="none" stroke="#1a5fc4" stroke-width=".8"/><path d="M2.4 3.2 5 5.3l2.6-2.1" fill="none" stroke="#1a5fc4" stroke-width=".8"/></svg>marissa@qlumiomarketing.example</li>
      <li><svg viewBox="0 0 10 10"><circle cx="5" cy="5" r="5" fill="#fff"/><circle cx="5" cy="5" r="2.6" fill="none" stroke="#1a5fc4" stroke-width=".7"/><path d="M2.4 5h5.2M5 2.4v5.2" stroke="#1a5fc4" stroke-width=".6"/></svg>www.qlumiomarketing.example</li>
      <li><svg viewBox="0 0 10 10"><circle cx="5" cy="5" r="5" fill="#fff"/><path d="M3 5.2 4.4 6.6 7 3.6" fill="none" stroke="#1a5fc4" stroke-width=".9"/></svg>License # 2187605-K</li>
    </ul>
  </section>

  <section class="card card-back" aria-label="Business card back">
    <p class="website-tagline">www.qlumiomarketing.example</p>
  </section>
</main>
</body>
</html>
```